Modern looking signage for dental office.

Exterior signage for passing cars
Target Market(s)
Cars passing by
Font styles to use
Sans Serif
Colors
3276b5
Requirements
Must have
- Logo
- OPEN ON SUTURDAY AND SUNDAY
- NIGHT CLINIC AVAILABLE
- PLEASE USE THE FONT TYPE IN FILE 4 UPLOADED BELOW.
- (482) 730-2964
- Modern looking

```html
<!DOCTYPE html>
<html lang="en">
<head>
<meta charset="utf-8">
<title>Summit Dental – Exterior Sign</title>
<link rel="stylesheet" href="https://fonts.googleapis.com/css2?family=Josefin+Sans:wght@300&family=Encode+Sans+Condensed:wght@400&family=Arimo:wght@700&display=swap">
<style>
  :root {
    --paper: #ffffff;
    --ink: #4a4546;
    --tagline: #5a5557;
    --teal: #0e87a0;
    --white: #ffffff;
    --icon-dark: #111111;
    --alert-red: #e8141b;
  }
  html, body {
    margin: 0;
    padding: 0;
    overflow: hidden;
    background: var(--paper);
  }
  .sign {
    position: relative;
    width: 1200px;
    height: 600px;
    overflow: hidden;
    background: var(--paper);
  }
  .brand {
    position: absolute;
    left: 0;
    top: 0;
    width: 1200px;
    height: 264px;
  }
  .brand-circle {
    position: absolute;
    left: 87px;
    top: 40px;
    width: 180px;
    height: 180px;
    box-sizing: border-box;
    border: 3px solid var(--ink);
    border-radius: 50%;
  }
  .brand-name {
    position: absolute;
    left: 292px;
    top: 78px;
    margin: 0;
    font-family: "Josefin Sans", sans-serif;
    font-weight: 300;
    font-size: 84px;
    line-height: 1;
    letter-spacing: 2px;
    color: var(--ink);
    white-space: nowrap;
  }
  .brand-tagline {
    position: absolute;
    left: 350px;
    top: 190px;
    width: 494px;
    margin: 0;
    text-align: center;
    font-family: "Encode Sans Condensed", sans-serif;
    font-weight: 400;
    font-size: 35px;
    line-height: 1;
    color: var(--tagline);
    white-space: nowrap;
  }
  .info-band {
    position: absolute;
    left: 0;
    top: 264px;
    width: 1200px;
    height: 336px;
    background: var(--teal);
  }
  .info-list {
    list-style: none;
    margin: 0;
    padding: 0;
  }
  .info-item {
    position: absolute;
    left: 150px;
    display: flex;
    align-items: center;
    height: 80px;
  }
  .info-item--hours { top: 48px; }
  .info-item--night { top: 152px; }
  .info-item--phone { top: 256px; transform: translateY(-8px); }
  .info-icon {
    width: 72px;
    height: 72px;
    flex: none;
    margin-right: 32px;
  }
  .info-text {
    font-family: "Arimo", sans-serif;
    font-weight: 700;
    font-size: 61px;
    line-height: 1;
    color: var(--white);
    white-space: nowrap;
  }
</style>
</head>
<body>
<main class="sign">
  <header class="brand">
    <div class="brand-circle"></div>
    <h1 class="brand-name">SUMMIT DENTAL</h1>
    <p class="brand-tagline">MODERN GENERAL DENTISTRY</p>
  </header>

  <section class="info-band">
    <ul class="info-list">
      <li class="info-item info-item--hours">
        <svg class="info-icon" viewBox="0 0 72 72" aria-hidden="true">
          <path d="M14 8 H46 V64 H42 V12 H18 V60 H14 Z" fill="var(--icon-dark)"/>
          <path d="M22 12 L56 6 V66 L22 60 Z" fill="var(--icon-dark)"/>
          <circle cx="28" cy="37" r="2" fill="var(--teal)"/>
        </svg>
        <span class="info-text">Open on Saturday and Sunday</span>
      </li>
      <li class="info-item info-item--night">
        <svg class="info-icon" viewBox="0 0 72 72" aria-hidden="true">
          <circle cx="36" cy="36" r="34" fill="var(--alert-red)"/>
          <rect x="30" y="18" width="12" height="36" fill="var(--white)"/>
          <rect x="18" y="30" width="36" height="12" fill="var(--white)"/>
        </svg>
        <span class="info-text">Night clinic available</span>
      </li>
      <li class="info-item info-item--phone">
        <svg class="info-icon" viewBox="0 0 72 72" aria-hidden="true">
          <circle cx="36" cy="36" r="32" fill="none" stroke="var(--icon-dark)" stroke-width="5"/>
          <path d="M25 19 c2-2 5-2 6 1 l3 7 c1 2 0 4-2 5 l-3 2 c2 5 6 9 11 11 l2-3 c1-2 3-3 5-2 l7 3 c3 1 3 4 1 6 l-3 3 c-3 3-8 3-13 0 C31 49 23 41 20 33 c-2-5-2-10 1-13 Z" fill="var(--icon-dark)"/>
        </svg>
        <span class="info-text">(482) 730-2964</span>
      </li>
    </ul>
  </section>
</main>
</body>
</html>
```